Plakat-Design für eine Werbeschild für ein Geflügelhof
Zielgruppe
Wir sind ein Geflügelhof, Landhandel, Hofladen, Eier stehen seit über 100 Jahren für Hof Kranwede, artgerechte Tierhaltung und Artikelvielfalt machen uns bekannt.
Aufgabenstellung
Das Werbeschild wird auf dem Hof aufgestellt und soll den Weg zum Hof zeigen.
- die Maße vom Schild: 1,50m breit x 2,40m hoch
- Grafiken werden als .ai und .pdf benötigt
- Logo ist hochgelagen
- Foto von unserer Vorstellung ist hochgeladen
Das Schild muss 400 m RECHTS drauf gedruckt haben.
Falls es zu breit wäre, könnte das Logo ja vielleicht auch über Hof Kranwede.
Das ganze wird bei plattenwerk auf eine MetoxPan-Platte in den Druck gegeben.

```html
<!DOCTYPE html>
<html lang="de">
<head>
<meta charset="utf-8">
<title>Hof Kranwede – Wegweiser</title>
<link href="https://fonts.googleapis.com/css2?family=Patrick+Hand&family=Roboto:wght@700;900&display=swap" rel="stylesheet">
<style>
  :root {
    --farm-green: #2a6e35;
    --signal-red: #c41e25;
    --white: #ffffff;
    --sky-top: #f7fafa;
    --sky-blue: #9fcbdb;
    --hill-green: #8fb84e;
    --field-dark: #4e5a3a;
    --field-green: #7c9a4c;
  }
  * { margin: 0; padding: 0; box-sizing: border-box; }
  html, body {
    width: 857px; height: 1200px; overflow: hidden;
    background: var(--white);
  }
  .canvas { position: relative; width: 857px; height: 1200px; }
  .sign {
    position: absolute; left: 146px; top: 146px;
    width: 566px; height: 902px;
    box-shadow: 0 0 14px rgba(0,0,0,0.35);
    overflow: hidden;
    background: var(--white);
  }
  .sky-scene {
    position: absolute; left: 0; top: 0; width: 100%; height: 462px;
    background:
      linear-gradient(180deg, transparent 0 380px, var(--hill-green) 395px, #6f9a3c 462px),
      linear-gradient(180deg, var(--sky-top) 0%, #fbfdfc 28%, var(--sky-blue) 40%, #d9ebec 60%, #f2f7f2 80%);
  }
  .brand-bar {
    position: absolute; left: 38px; top: 51px; width: 489px; height: 89px;
    background: var(--white);
    display: flex; align-items: center; gap: 16px; padding-left: 3px;
  }
  .brand-dot {
    width: 84px; height: 84px; border-radius: 50%;
    background: var(--farm-green); flex: none;
  }
  .brand-name {
    font-family: "Patrick Hand", cursive;
    font-size: 62px; color: var(--farm-green); line-height: 1;
    white-space: nowrap;
  }
  .headline {
    position: absolute; left: 0; top: 180px; width: 100%;
    text-align: center;
    font-family: "Patrick Hand", cursive;
    font-weight: 400; font-size: 112px; line-height: 86px;
    color: var(--farm-green);
  }
  .headline span { display: block; }
  .headline .line-two { padding-left: 40px; }
  .direction-band {
    position: absolute; left: 0; top: 462px; width: 100%; height: 162px;
    background: var(--signal-red);
    display: flex; align-items: center; justify-content: center;
    font-family: "Roboto", sans-serif; font-weight: 900;
    font-size: 76px; color: var(--white); letter-spacing: 1px;
  }
  .field-scene {
    position: absolute; left: 0; top: 624px; width: 100%; height: 278px;
    background:
      linear-gradient(180deg, rgba(126,154,76,0.9) 0%, rgba(95,120,60,0.85) 50%, rgba(90,80,60,0.95) 100%),
      var(--field-dark);
  }
  .animal-gallery {
    position: absolute; left: 32px; top: 664px;
    display: flex; gap: 10px;
  }
  .animal-tile {
    width: 154px; height: 171px;
    border: 5px solid var(--white);
  }
  .animal-tile.cow { background: linear-gradient(180deg, #2f4a2a 0%, #4f7a35 35%, #6c9a3e 100%); }
  .animal-tile.duck { background: linear-gradient(180deg, #c9d6b4 0%, #8fae5a 40%, #e9ece6 55%, #5e7f3a 100%); }
  .animal-tile.hens { background: linear-gradient(180deg, #8c9077 0%, #7a9a4a 40%, #a2552a 70%, #6f8a3e 100%); }
</style>
</head>
<body>
<div class="canvas">
  <div class="sign">
    <div class="sky-scene" role="img" aria-label="Heller Himmel mit Wolken über grünen Hügeln"></div>
    <div class="brand-bar">
      <div class="brand-dot"></div>
      <div class="brand-name">Hof Kranwede</div>
    </div>
    <h1 class="headline">
      <span class="line-one">Einkauf auf</span>
      <span class="line-two">dem Bauernhof</span>
    </h1>
    <div class="direction-band">400M RECHTS</div>
    <div class="field-scene" role="img" aria-label="Grüne Felder mit Pflanzenreihen"></div>
    <div class="animal-gallery">
      <div class="animal-tile cow" role="img" aria-label="Kuh grast auf einer Weide"></div>
      <div class="animal-tile duck" role="img" aria-label="Weiße Ente auf der Wiese"></div>
      <div class="animal-tile hens" role="img" aria-label="Braune Hühner im Gras"></div>
    </div>
  </div>
</div>
</body>
</html>
```